Refresh existing website - qfamdv.org

Apply these upgrades to the existing website
1. Modern Design: Update the overall aesthetic to a clean, contemporary look with bold typography,
vibrant colors, and improved visual hierarchy.
2. Mobile Optimization: Enhance responsiveness for seamless navigation on mobile devices.
3. Intuitive User Interface: Simplify navigation by reducing menu complexity and improving call-to-
action buttons.
4. SEO Optimization: Improve content for better ranking on search engines.
5. Accessibility: Ensure compliance with WCAG standards for inclusivity.
6. Faster Load Times: Optimize images and scripts for better performance.
7. Social Media Integration: Add live social media feeds to showcase community engagement.
8. Prefer html
Industry/Entity Type
Consulting
Coding
Coded - Design and coding required
Number of Pages Required
5+ page
Look and feel

```html
<!DOCTYPE html>
<html lang="en">
<head>
<meta charset="utf-8">
<title>NACHPA – Healthcare Practice Advisors</title>
<link href="https://fonts.googleapis.com/css2?family=Montserrat:wght@400;500;600;700&display=swap" rel="stylesheet">
<style>
:root{
  --slate:#455a6e;
  --slate-dark:#3a4d60;
  --green:#6b8e23;
  --ink:#333;
  --muted:#555;
  --light:#eef0f3;
  --footer:#232323;
  --white:#fff;
}
*{box-sizing:border-box;margin:0;padding:0}
html,body{width:1200px;height:4812px;overflow:hidden}
body{font-family:'Montserrat',sans-serif;color:var(--ink);background:var(--white);position:relative}
.abs{position:absolute}
.topbar{height:34px;background:var(--slate);color:#fff;font-size:15px;display:flex;justify-content:space-between;align-items:center;padding:0 110px}
.header{height:117px;display:flex;align-items:center;justify-content:space-between;padding:0 110px}
.brand{display:flex;align-items:center;gap:12px}
.brand-mark{width:22px;height:22px;background:var(--green)}
.brand-name{font-weight:700;font-size:40px;color:var(--slate);letter-spacing:1px}
.nav{display:flex;gap:20px;font-size:17px;font-weight:500;color:#333}
.hero{height:660px;background:linear-gradient(160deg,#5b6f86 0%,#3d4c5e 40%,#7a5a38 75%,#4b3521 100%);position:relative}
.hero h1{position:absolute;left:110px;top:368px;color:#fff;font-size:47px;font-weight:700;line-height:54px;width:800px}
.btn{display:inline-flex;align-items:center;justify-content:center;border-radius:32px;font-weight:600;font-size:17px;text-transform:uppercase}
.btn-white{background:#fff;color:#222}
.btn-ghost{border:2px solid #fff;color:#fff}
.btn-green{background:var(--green);color:#fff}
.hero .btn{position:absolute;top:514px;height:62px}
.welcome{height:652px;position:relative}
.frame{position:absolute;left:110px;top:81px;width:443px;height:482px;border:2px solid #bbb}
.frame .photo{position:absolute;left:16px;top:16px;right:16px;bottom:16px;background:linear-gradient(135deg,#8fa2b8,#c9c3b9 55%,#6b7b8f)}
h2{font-weight:700;color:var(--slate)}
.welcome h2{position:absolute;left:632px;top:88px;font-size:40px}
.welcome p{position:absolute;left:632px;top:158px;width:460px;font-size:15.5px;line-height:27.5px;color:var(--muted)}
.welcome .btn{position:absolute;left:632px;top:495px;width:149px;height:54px;font-size:16px}
.events{height:896px;background:var(--light);position:relative}
.center-title{position:absolute;left:0;right:0;text-align:center;font-size:40px}
.pricebar{position:absolute;left:159px;top:165px;width:882px;height:84px;display:flex;color:#fff;font-size:20px;font-weight:500;text-align:center;line-height:28px}
.pricebar div{flex:1;display:flex;align-items:center;justify-content:center}
.card{position:absolute;top:301px;width:314px;height:454px;background:#fff;box-shadow:0 2px 6px rgba(0,0,0,.08)}
.card .photo{height:239px}
.card h3{font-size:18px;font-weight:500;line-height:26px;margin:24px 28px 0;color:#333}
.card .price{margin:28px 28px 0;color:var(--green);font-weight:700;font-size:17px}
.card .member{margin:10px 28px 0;font-style:italic;font-size:15px;color:#444}
.dots{position:absolute;top:808px;left:0;right:0;display:flex;justify-content:center;gap:8px}
.dots span{width:11px;height:11px;border-radius:50%;border:1px solid #888}
.dots span.on{background:#777}
.foundation{height:540px;background:var(--slate);position:relative;color:#fff}
.foundation h2{color:#fff;position:absolute;left:110px;top:88px;width:520px;font-size:40px;line-height:48px}
.foundation p{position:absolute;left:110px;top:268px;width:470px;font-size:15.5px;line-height:27.5px}
.foundation .btn{position:absolute;left:110px;top:399px;width:148px;height:54px;font-size:16px}
.foundation .photo{position:absolute;left:665px;top:89px;right:0;bottom:0;background:linear-gradient(135deg,#b9c7d6,#7e92a8 50%,#d7dde4)}
.social{height:811px;position:relative}
.post{position:absolute;top:177px;width:471px}
.post .photo{height:324px}
.post .meta{display:flex;align-items:center;margin-top:20px;gap:14px}
.avatar{width:70px;height:70px;border-radius:50%;background:#f0f0f0;border:1px solid #ddd;display:flex;align-items:center;justify-content:center;font-size:13px;font-weight:700;color:#555}
.post .who{font-size:19px;font-weight:500;line-height:25px;flex:1}
.net{width:50px;height:50px;border-radius:50%}
.post p{margin-top:22px;font-size:15.5px;line-height:29px;color:var(--muted)}
.arrow{position:absolute;top:316px;width:46px;height:46px;border-radius:50%;border:1px solid #ccc;display:flex;align-items:center;justify-content:center}
.sponsors{height:348px;position:relative}
.logos{position:absolute;top:168px;left:110px;display:flex;gap:11px}
.logos div{width:153px;height:94px;border:1px solid #999;display:flex;align-items:center;justify-content:center;font-size:22px;font-weight:600;color:#333}
.cta{height:321px;background:var(--green);position:relative;color:#fff;text-align:center}
.cta h2{color:#fff;position:absolute;left:0;right:0;top:62px;font-size:40px}
.cta p{position:absolute;left:0;right:0;top:128px;font-size:16px}
.cta .btn{position:absolute;left:476px;top:188px;width:249px;height:53px;font-size:16px}
.footer{height:433px;background:var(--footer);color:#fff;position:relative}
.footer .brand{position:absolute;left:110px;top:108px}
.footer .brand-name{color:#fff}
.socials{position:absolute;left:110px;top:193px;display:flex;gap:11px}
.socials span{width:50px;height:50px;border-radius:50%;border:2px solid #ccc}
.fcol{position:absolute;top:43px;font-size:15.5px;line-height:33px}
.fcol h4{font-size:17px;font-weight:600;margin-bottom:12px}
.fcol .row{display:flex;gap:12px;align-items:flex-start;line-height:24px;margin-bottom:24px}
.copyright{position:absolute;left:110px;right:110px;top:350px;border-top:1px solid #555;padding-top:32px;text-align:center;font-size:15.5px}
</style>
</head>
<body>
<div class="topbar"><span>Get Certified | Practice Reports | Institute (IPML)</span><span>Contact Us 555-010-2741 | Member Login</span></div>
<header class="header">
  <div class="brand"><span class="brand-mark"></span><span class="brand-name">NACHPA</span></div>
  <nav class="nav"><span>About</span><span>Upcoming Events</span><span>Resources</span><span>Sponsors</span><span>Contact</span></nav>
</header>

<section class="hero" role="img" aria-label="Healthcare professionals meeting around a conference table with laptops">
  <h1>We are the Professionals in the Business of Healthcare</h1>
  <span class="btn btn-white" style="left:110px;width:232px">Join NACHPA Today!</span>
  <span class="btn btn-ghost" style="left:351px;width:232px">Find a Consultant</span>
</section>

<section class="welcome">
  <div class="frame"><div class="photo" role="img" aria-label="Medical staff reviewing work on a laptop"></div></div>
  <h2>Welcome to NACHPA</h2>
  <p>For nearly 30 years, the National Alliance of Certified Healthcare Practice Advisors (NACHPA) and its originating organizations have provided an active forum for networking and knowledge sharing. NACHPA provides members with an in-depth understanding of the constantly changing healthcare business environment – both medical and dental – that is unavailable anywhere else. At our core is the belief that knowledge is gained via continuous professional development, which grows exponentially when we share it with our fellow members through the exchange of insights and best practices.</p>
  <span class="btn btn-green">Read More</span>
</section>

<section class="events">
  <h2 class="center-title" style="top:76px">Upcoming Events</h2>
  <div class="pricebar">
    <div style="background:var(--slate)">Bundle – four webinars -<br>$159 members, $249 non-members</div>
    <div style="background:var(--green)">Single webinars -<br>$49 members, $99 non-members</div>
  </div>
  <article class="card" style="left:110px">
    <div class="photo" role="img" aria-label="Medicare paperwork on a desk" style="background:linear-gradient(135deg,#f2f2f2,#c9b89a)"></div>
    <h3>2024 Medicare Quarterly Updates Webinar - 3rd Quarter – September 24th at 11:00AM EDT</h3>
    <div class="price">$99.00</div><div class="member">$49.00 - Member price</div>
  </article>
  <article class="card" style="left:443px">
    <div class="photo" role="img" aria-label="Binders labelled compliance and regulations" style="background:linear-gradient(135deg,#3d6fb8,#e5e8ee 55%,#c7a84a)"></div>
    <h3>2024 Medicare Quarterly Updates Webinar - 4th Quarter – December 10th at 11:00AM EST</h3>
    <div class="price">$99.00</div><div class="member">$49.00 - Member price</div>
  </article>
  <article class="card" style="left:776px">
    <div class="photo" role="img" aria-label="Medical cross with heartbeat line over documents" style="background:linear-gradient(135deg,#a9c4dd,#e8eef5 50%,#d9a5b0)"></div>
    <h3>Medicare Quarterly Updates Webinars - 4 Webinar Bundle</h3>
    <div class="price" style="margin-top:54px">$249.00</div><div class="member">$159.00 - Member price</div>
  </article>
  <div class="dots"><span class="on"></span><span></span><span></span><span></span><span></span></div>
</section>

<section class="foundation">
  <h2>The Institute for Practice Management Learning</h2>
  <p>The Institute for Practice Management Learning is a non-profit organization dedicated to improving healthcare delivery through the education of practice management consultants.</p>
  <span class="btn btn-green">Donate</span>
  <div class="photo" role="img" aria-label="Team stacking hands together"></div>
</section>

<section class="social">
  <h2 class="center-title" style="top:74px">Social Media</h2>
  <div class="arrow" style="left:35px"><svg width="14" height="14" viewBox="0 0 14 14"><path d="M9 2 4 7l5 5" fill="none" stroke="#555" stroke-width="1.6"/></svg></div>
  <div class="arrow" style="left:1119px"><svg width="14" height="14" viewBox="0 0 14 14"><path d="M5 2l5 5-5 5" fill="none" stroke="#555" stroke-width="1.6"/></svg></div>
  <article class="post" style="left:110px">
    <div class="photo" role="img" aria-label="Business handshake with network lines" style="background:linear-gradient(135deg,#2f4a6e,#8fb0cf 60%,#dfe8f1)"></div>
    <div class="meta"><div class="avatar">BRISK</div><div class="who">Finibus Bonorum<br>et Malorum</div><span class="net" style="background:#3b5998"></span></div>
    <p>Duis aute irure dolor in reprehenderit in voluptate velit esse cillum dolore eu fugiat nulla pariatur. Excepteur sint occaecat cupidatat non proident, sunt in culpa qui officia deserunt mollit anim id est laborum.</p>
  </article>
  <article class="post" style="left:619px">
    <div class="photo" role="img" aria-label="Video of colleagues reviewing charts beside a laptop" style="background:linear-gradient(135deg,#d8d8d8,#9a9a9a 50%,#efefef);position:relative">
      <svg class="abs" style="left:203px;top:130px" width="64" height="64" viewBox="0 0 64 64"><circle cx="32" cy="32" r="32" fill="#222"/><path d="M26 20v24l19-12z" fill="#fff"/></svg>
    </div>
    <div class="meta"><div class="avatar">BRISK</div><div class="who">Finibus Bonorum<br>et Malorum</div><span class="net" style="background:#e02424"></span></div>
    <p>Duis aute irure dolor in reprehenderit in voluptate velit esse cillum dolore eu fugiat nulla pariatur. Excepteur sint occaecat cupidatat non proident, sunt in culpa qui officia deserunt mollit anim id est laborum.</p>
  </article>
</section>

<section class="sponsors">
  <h2 class="center-title" style="top:74px">NACHPA Sponsors</h2>
  <div class="logos"><div>HALDEN</div><div>TRIVANE</div><div>MEDRIX</div><div>NORVA</div><div>CLEARWELL</div><div>VERITY</div></div>
</section>

<section class="cta">
  <h2>Become an Exhibitor or Annual Sponsor</h2>
  <p>Sign-up now to take advantage of the Early Bird rates thru January! A $250 savings!</p>
  <span class="btn btn-white">Join NACHPA Today!</span>
</section>

<footer class="footer">
  <div class="brand"><span class="brand-mark"></span><span class="brand-name" style="font-size:56px">NACHPA</span></div>
  <div class="socials"><span></span><span></span><span></span><span></span></div>
  <div class="fcol" style="left:566px"><h4>Contact Information</h4>Home<br>About<br>Upcoming Events<br>Resources<br>Sponsors<br>Contact</div>
  <div class="fcol" style="left:867px"><h4>Contact Information</h4>
    <div class="row" style="margin-bottom:4px">NACHPA</div>
    <div class="row"><svg width="12" height="16" viewBox="0 0 12 16"><path d="M6 0a6 6 0 0 0-6 6c0 4 6 10 6 10s6-6 6-10a6 6 0 0 0-6-6zm0 8.5A2.5 2.5 0 1 1 6 3.5a2.5 2.5 0 0 1 0 5z" fill="var(--green)"/></svg><span>2480 Linden Commons Dr.<br>#120 Fairview, VA 20100</span></div>
    <div class="row"><svg width="14" height="14" viewBox="0 0 14 14"><path d="M3 1l3 3-2 2c1 2 2 3 4 4l2-2 3 3-2 2C6 13 1 8 1 3z" fill="var(--green)"/></svg><span>Tel: 555-010-2741</span></div>
    <div class="row"><svg width="14" height="14" viewBox="0 0 14 14"><rect x="1" y="4" width="12" height="8" fill="var(--green)"/><rect x="4" y="1" width="6" height="4" fill="var(--green)"/></svg><span>Fax: 555-010-4390</span></div>
    <div class="row"><svg width="14" height="12" viewBox="0 0 14 12"><rect width="14" height="12" fill="var(--green)"/><path d="M0 0l7 6 7-6" fill="none" stroke="#232323" stroke-width="1.5"/></svg><span>info@qfamdv.org</span></div>
  </div>
  <div class="copyright">©2024 National Alliance of Certified Healthcare Practice Advisors | Privacy Policy | Site Disclaimer | Sitemap</div>
</footer>
</body>
</html>
```